Ecommerce Site Makeover

We will be migrating our website from QV Retail to Magento and need a complete makeover. Here are the pages that need to be redesigned.
1. Home Page + Navigational Menu
2. Product page
3. Category page/category layered navigation
4. Brand page directory
5. Internal brand page
6. Sales emails
7. Internal pages (logged in)
8. Cart Page
9. Checkout Pages/Flow
The current site is at www.bluemarrowcrafts.example. We will be using Magento as the new platform, so you can check out the default magento site here:
http://demo.lorvexstore.example to get an idea how the stock product pages, category pages, cart pages, checkout currently function and which information is listed there. Please make sure to create an account and login so that you understand the functionality there
We are a baby boutique, so we want the site to be emotionally appealing. For the brand page and brand directory, here is a good example: http://www.kavrelo.example/brands and http://www.kavrelo.example/brands/silent-orchard
Here are some good navigation examples:
http://www.dunmoreshades.example/
http://www.hollenbrook.example
http://www.peverillgreetings.example/
Here is a good example of great uses of layered navigation (on left Narrow Selection)
http://www.hollenbrook.example/Crib-Bedding-Sets-C837264.html
http://www.trevunda.example/girls-dresses~1p
Here is a good example of product page design complete with user feedback integration:
http://www.trevunda.example/product/4815093/color/582730
I will like the product page to be designed with similar social/user content integration.
In addition, we will utiize the kestrel/lumacert trust seal in the template and especially on cart and checkout pages. In addition, we need to create a "Seal" similar to www.ordertrust.example which will reside in the bottom right hand side of the site like www.ordertrust.example - We will call ours Cart Haven
Updates
Hello Neil. Deadline is fast approaching and I am in dire need of a makeover for my site. Are you still planning on submitting a design for my project? Please let me know either way. Thanks!
Industry/Entity Type
Baby
Look and feel
Each slider illustrates characteristics of the customer's brand and the style your logo design should communicate.

```html
<!DOCTYPE html>
<html lang="en">
<head>
<meta charset="utf-8">
<title>Blue Marrow Crafts – Checkout</title>
<link href="https://fonts.googleapis.com/css2?family=Mulish:wght@400;600;700&family=Delius&family=Great+Vibes&display=swap" rel="stylesheet">
<style>
:root{
  --bg-pink:#f8c6da;
  --pink:#e8468a;
  --pink-soft:#f27cb0;
  --pink-light:#fbd9e7;
  --blue:#bfe3f5;
  --blue-soft:#d6eefa;
  --blue-deep:#3ba7dd;
  --cream:#f8f6ef;
  --brown:#5a3a22;
  --text:#444;
  --grey:#777;
  --white:#fff;
}
*{box-sizing:border-box;margin:0;padding:0}
html,body{width:1200px;height:1055px;overflow:hidden}
body{background:var(--bg-pink);font-family:"Mulish",sans-serif;color:var(--text);position:relative}
.abs{position:absolute}
.page{left:132px;top:12px;width:938px;height:1036px;background:var(--white)}
.header{left:0;top:0;width:938px;height:144px;background:var(--white)}
.logo{left:20px;top:22px;display:flex;align-items:center;gap:10px;font-family:"Delius",cursive;font-size:27px;color:var(--brown)}
.logo .dot{width:34px;height:34px;border-radius:50%;background:var(--pink-light)}
.tagline{left:20px;top:104px;font-family:"Delius",cursive;font-size:19px;color:var(--brown)}
.deco{border-radius:40%}
.account{left:478px;top:30px;list-style:none;font-size:12.5px;color:var(--pink)}
.account li{display:flex;align-items:center;gap:6px;height:20px}
.account li::before{content:"";width:12px;height:12px;border-radius:50%;background:#b8d86a}
.stroller-title{left:668px;top:10px;font-size:14px;color:var(--pink);letter-spacing:.5px}
.count{left:760px;top:70px;width:36px;height:36px;border-radius:50%;border:3px solid #f5a640;background:var(--white);font-size:15px;text-align:center;line-height:30px}
.items{left:805px;top:74px;font-size:12px;color:var(--pink);font-weight:700}
.cart-btn{left:850px;top:73px;width:72px;height:17px;border-radius:4px;background:var(--pink);color:var(--white);font-size:12px;text-align:center;line-height:17px}
.trust-badge{left:820px;top:8px;width:104px;height:56px;border-radius:8px;background:#f2f2f2;border:2px solid #e0a020}
.nav{left:0;top:144px;width:938px;height:42px;background:var(--pink-soft);display:flex;align-items:center;padding-left:18px;gap:24px}
.nav a{color:var(--white);font-size:18px;text-decoration:none}
.search{left:686px;top:151px;width:242px;height:29px;border-radius:15px;background:var(--white);font-size:12px;color:#555;padding:7px 14px}
.search span{position:absolute;right:4px;top:4px;width:21px;height:21px;border-radius:50%;background:var(--blue-deep)}
.band{left:0;top:186px;width:938px;height:30px;background:var(--blue)}
.main{left:0;top:216px;width:938px;height:486px;background:var(--cream)}
.title{left:13px;top:26px;font-family:"Great Vibes",cursive;font-size:34px;color:var(--pink)}
.steps{left:8px;top:84px;display:flex;gap:6px}
.step{width:154px;height:56px;background:var(--blue-soft);border-radius:6px;display:flex;align-items:center;gap:6px;padding-left:8px;color:#a8cde0;font-size:16.5px;line-height:1.05}
.step b{font-size:30px;font-style:italic;font-weight:400}
.step.active{background:var(--pink);color:var(--white);width:132px}
.box{top:162px;width:367px;height:278px;background:var(--blue-soft);border:5px solid #e8f6fd;border-radius:6px;padding:20px 40px;font-size:13px}
.box h2{font-weight:400;font-size:16px;color:var(--pink);margin-bottom:8px}
.box p{margin-bottom:6px}
.radio{display:flex;align-items:center;gap:7px;margin:9px 0}
.radio i{width:11px;height:11px;border-radius:50%;border:1px solid #999;background:var(--white)}
.radio i.on{background:radial-gradient(#333 35%,var(--white) 40%)}
.box ul{list-style:none;margin-top:8px}
.box li::before{content:"‣ ";color:#777}
.btn{display:inline-block;background:var(--pink-soft);color:var(--white);border-radius:12px;height:24px;line-height:24px;text-align:center;font-size:13.5px}
.field{width:290px;height:28px;background:var(--white);border:1px solid #cde;border-radius:4px;margin:6px 0 16px}
.req{color:var(--pink)}
.signup{left:20px;top:490px;width:532px;height:72px;background:var(--pink-light);border-radius:4px}
.signup h3{position:absolute;left:25px;top:10px;font-family:"Delius",cursive;font-weight:400;font-size:23px;line-height:1.05;color:var(--pink)}
.signup .input{position:absolute;left:182px;top:18px;width:340px;height:32px;border-radius:16px;background:var(--white)}
.signup .btn{position:absolute;left:446px;top:20px;width:78px;height:28px;line-height:28px;border-radius:14px;background:var(--pink);font-weight:700;font-size:13px}
.footer-line{left:0;top:794px;width:938px;height:6px;border-top:3px dotted var(--pink-soft);border-bottom:2px solid var(--pink-soft)}
.col{top:854px;font-size:12.5px;line-height:19.3px;color:#6b3a22}
.col h4{font-family:"Delius",cursive;font-weight:400;font-size:17.5px;color:var(--pink);margin-bottom:4px}
.bottom{left:0;top:988px;width:938px;height:4px;border-top:2px dotted var(--pink-soft)}
.copy{left:0;top:1004px;width:938px;text-align:center;font-size:12px;color:#3a6fb0}
.seal{left:690px;top:658px;width:490px;height:330px;background:var(--white);border:1px solid #ccc;box-shadow:0 2px 8px rgba(0,0,0,.25);font-size:12.5px;color:#333}
.seal-head{height:68px;background:#f4f4f4;border-bottom:1px solid #ddd;position:relative}
.seal-brand{position:absolute;left:14px;top:14px;display:flex;align-items:center;gap:8px;font-weight:700;font-size:14px;line-height:1.1}
.seal-brand i{width:36px;height:36px;border-radius:50%;background:#7cc242}
.seal-head h3{position:absolute;left:160px;top:14px;font-size:17px;width:320px;text-align:center}
.seal-head p{position:absolute;left:160px;top:38px;font-size:15px;width:320px;text-align:center;color:#555}
.seal-intro{padding:12px 18px 6px}
.feat{display:flex;gap:12px;padding:9px 18px 0 20px;align-items:flex-start}
.feat svg{flex:none;margin-top:2px}
.feat b{display:block;font-size:14px}
.feat small{font-size:11.5px}
.passes{position:absolute;left:0;bottom:0;width:100%;height:52px;border-top:1px solid #ddd;background:#f6f6f6;display:flex;justify-content:space-around;align-items:center;font-size:11.5px}
.pass{display:flex;gap:6px;align-items:center}
.pass i{width:22px;height:26px;border-radius:4px}
.seal-tab{left:1080px;top:998px;width:118px;height:54px;background:var(--white);border:1px solid #ccc;display:flex;align-items:center;gap:6px;padding:6px;font-size:12.5px;font-weight:700;line-height:1.1}
.seal-tab i{width:34px;height:34px;border-radius:50%;background:#7cc242;flex:none}
</style>
</head>
<body>
<div class="abs page">
  <header class="abs header">
    <div class="abs logo"><span class="dot"></span>Blue Marrow Crafts</div>
    <div class="abs tagline">Unique Children's Boutique</div>
    <div class="abs deco" role="img" aria-label="Illustration of a baby bib and bonnet" style="left:280px;top:70px;width:110px;height:50px;background:#f9e6b8"></div>
    <div class="abs deco" role="img" aria-label="Illustration of a baby rattle" style="left:560px;top:82px;width:40px;height:50px;background:#d6ecf8"></div>
    <ul class="abs account"><li>My Account</li><li>My Wishlist</li><li>My Cart</li><li>Log In</li></ul>
    <div class="abs stroller-title">YOUR STROLLER</div>
    <div class="abs deco" role="img" aria-label="Illustration of a blue baby stroller" style="left:664px;top:36px;width:76px;height:100px;background:#7fc8ee"></div>
    <div class="abs deco" role="img" aria-label="Illustration of a bumble bee" style="left:754px;top:32px;width:48px;height:36px;background:#c6e07a"></div>
    <div class="abs count">0</div>
    <div class="abs items">ITEMS</div>
    <div class="abs cart-btn">Checkout</div>
    <div class="abs trust-badge" role="img" aria-label="Kestrel Lumacert security seal"></div>
  </header>
  <nav class="abs nav"><a>Home</a><a>Baby</a><a>Girls</a><a>Boys</a><a>Gifts &amp; Occasions</a><a>What's New</a><a>Contact</a></nav>
  <div class="abs search">Search<span></span></div>
  <div class="abs band" role="img" aria-label="Decorative band of little ducks"></div>

  <main class="abs main">
    <h1 class="abs title">Checkout</h1>
    <div class="abs deco" role="img" aria-label="Illustration of a safety pin with a teddy bear" style="left:876px;top:20px;width:40px;height:46px;background:#bfe3f5"></div>
    <div class="abs steps">
      <div class="step active"><b>1</b>Checkout<br>Method</div>
      <div class="step"><b>2</b>Billing<br>Information</div>
      <div class="step"><b>3</b>Shipping<br>Information</div>
      <div class="step"><b>4</b>Shipping<br>Method</div>
      <div class="step"><b>5</b>Payment<br>Information</div>
      <div class="step"><b>6</b>Order<br>Review</div>
    </div>
    <section class="abs box" style="left:60px">
      <h2>Checkout as a Guest or Register</h2>
      <p>Register with us for future convenience:</p>
      <div class="radio"><i></i>Checkout as Guest</div>
      <div class="radio"><i class="on"></i>Register</div>
      <p style="margin-top:14px;color:#222">Register and save time!<br><span style="color:#444">Register with us for future convenience:</span></p>
      <ul><li>Fast and easy check out</li><li>Easy access to your order history and status</li></ul>
      <span class="btn" style="width:148px;margin-top:12px;margin-left:-4px">Continue</span>
    </section>
    <section class="abs box" style="left:504px;padding-left:24px">
      <h2>Login</h2>
      <p>Already registered?<br>Please log in below:</p>
      <p>E-Mail Address<span class="req">*</span></p>
      <div class="field"></div>
      <p>Password<span class="req">*</span></p>
      <div class="field"></div>
      <span class="btn" style="width:82px">Login</span>
      <span style="margin-left:60px">Forgot your password?</span>
    </section>
    <div class="abs signup">
      <h3>Sign Up For<br>Special Offers</h3>
      <div class="input"></div>
      <span class="btn">SIGN UP</span>
    </div>
    <div class="abs deco" role="img" aria-label="Illustration of a baby onesie" style="left:264px;top:470px;width:42px;height:26px;background:#f9d48a"></div>
  </main>

  <div class="abs footer-line"></div>
  <div class="abs deco" role="img" aria-label="Illustration of a hanging crib mobile" style="left:264px;top:776px;width:90px;height:110px;background:#cfe8f5"></div>
  <div class="abs col" style="left:28px"><h4>Quick Link's</h4>Home<br>About Us<br>Search Terms<br>Advanced Search<br>Orders and Returns</div>
  <div class="abs col" style="left:174px"><h4>Shop By Category</h4>Baby<br>Girls<br>Boys<br>Birthday Boutique<br>Gifts &amp; Occasions</div>
  <div class="abs col" style="left:350px"><h4>Shop By Brand</h4>Snugglo Wipes<br>Pacifo Sparkle<br>Wrenly Covers<br>Maplesprout, Hushbee Bags<br>Tiny Tallow</div>
  <div class="abs col" style="left:524px"><h4>Help</h4>Site Map<br>Accessibility<br>Security<br>FAQs<br>Our Warranty</div>
  <div class="abs bottom"></div>
  <div class="abs copy">© 2012 Blue Marrow Crafts. All rights reserved.</div>
</div>

<aside class="abs seal">
  <div class="seal-head">
    <div class="seal-brand"><i></i>Cart Haven<br>Protected<br>Store</div>
    <h3>Satisfaction and Security Guaranteed</h3>
    <p>Your Transaction Is Protected</p>
  </div>
  <p class="seal-intro">Cart Haven certifies that this merchant is qualified to provide a protected shopping experience.</p>
  <div class="feat"><svg width="20" height="22" viewBox="0 0 20 22"><path d="M10 1 L18 4 V10 C18 15 14 19 10 21 C6 19 2 15 2 10 V4 Z" fill="none" stroke="#2a5db0" stroke-width="2"/></svg><div><b>Fraud Protection</b><small>Receive comprehensive fraud protection</small></div></div>
  <div class="feat"><svg width="22" height="20" viewBox="0 0 22 20"><path d="M1 2 H5 L8 13 H18 L21 5 H6" fill="none" stroke="#2a5db0" stroke-width="2"/><circle cx="9" cy="17" r="2" fill="#2a5db0"/><circle cx="17" cy="17" r="2" fill="#2a5db0"/></svg><div><b>Purchase Protection</b><small>Purchase with confidence and security protection</small></div></div>
  <div class="feat"><svg width="22" height="20" viewBox="0 0 22 20"><circle cx="7" cy="10" r="6" fill="none" stroke="#2a5db0" stroke-width="2"/><circle cx="15" cy="10" r="6" fill="none" stroke="#2a5db0" stroke-width="2"/></svg><div><b>Lowest Price Protection</b><small>Lowest purchase price protection for 30 days</small></div></div>
  <div class="passes">
    <div class="pass"><i style="background:#e0a020"></i><div><b>Security Protected</b><br>Passed 08/12/2012</div></div>
    <div class="pass"><i style="background:#2a5db0;border-radius:50%"></i><div><b>Privacy Protected</b><br>Passed 08/12/2012</div></div>
    <div class="pass"><i style="background:#4aa83a"></i><div><b>Satisfaction Protected</b><br>Passed 08/12/2012</div></div>
  </div>
</aside>
<div class="abs seal-tab"><i></i><span>Cart Haven<br>Protected<br>Store</span></div>
</body>
</html>
```